Klassisches Visitenkarten-Design mit braunen Farbtönen gesucht
Zielgruppe
Meine Firma bietet Pferdezahnbehandlungen, Pferdefütterungsberatung sowie Trensen- und Gebissanpassungen an. Ausserdem habe ich eine mobile Pferdewaage. Meine Kunden sind Pferdebesitzer der gehobenen Klasse, die gerne Geld in die Hand nehmen um ihr Tier korrekt zu halten/versorgen.
Ich setze bisher auf ein klassisches Design in braun Tönen.
Aufgabenstellung
Mir ist eine klare, schnörkellose Botschaft wichtig.
Ich möchte mich gerne mit klassischem, aber auch sehr schönem Design von der Konkurrenz abheben.
Der Fokus soll auf der wissenschaftlichen Arbeitsweise mit dem Partner Pferd liegen.
Im Anhang sind Fotos von der alten Visitenkarten. Dort fehlt mir aber die klare Linie.
Normalerweise arbeite ich mit der Schriftart Eurostyle, bin aber auch für neue Vorschläge offen.

```html
<!DOCTYPE html>
<html lang="de">
<head>
<meta charset="utf-8">
<title>Equivita – Visitenkarte</title>
<link rel="stylesheet" href="https://fonts.googleapis.com/css2?family=Michroma&family=Saira:wght@300;400&display=swap">
<style>
  :root {
    --brown: #6b2a0c;
    --brown-text: #6b2a0c;
    --paper: #ffffff;
    --backdrop: #f1efed;
    --shadow: rgba(60, 30, 10, 0.18);
  }
  * { margin: 0; padding: 0; box-sizing: border-box; }
  html, body {
    width: 1200px; height: 873px; overflow: hidden;
    background: var(--backdrop);
  }
  .sheet {
    position: relative; width: 1200px; height: 873px;
    display: flex; justify-content: center; align-items: center; gap: 70px;
  }
  .card {
    position: relative; width: 340px; height: 520px;
    background: var(--paper);
    box-shadow: 0 10px 30px var(--shadow);
    overflow: hidden;
    display: flex; flex-direction: column;
  }
  .brown-field { background: var(--brown); color: var(--paper); }

  /* front */
  .front .brown-field {
    height: 355px;
    display: flex; align-items: center; justify-content: center; gap: 14px;
  }
  .mark-dot { width: 22px; height: 22px; border-radius: 50%; background: var(--paper); }
  .mark-name {
    font-family: "Michroma", sans-serif; font-size: 26px; letter-spacing: 2px;
    color: var(--paper);
  }
  .front .white-field {
    flex: 1; padding: 36px 0 0 38px; color: var(--brown-text);
  }
  .brand {
    font-family: "Michroma", sans-serif; font-size: 34px; letter-spacing: 2px;
    line-height: 1; margin-bottom: 16px;
  }
  .services {
    list-style: none; font-family: "Saira", sans-serif; font-weight: 300;
    text-transform: uppercase; letter-spacing: 0.5px;
  }
  .services li { font-size: 14px; line-height: 1.45; }
  .services li.lead { font-size: 18px; font-weight: 400; line-height: 1.3; }

  /* back */
  .back .white-field {
    height: 250px; padding: 70px 30px 0 0;
    display: flex; flex-direction: column; align-items: flex-end;
    color: var(--brown-text);
  }
  .back .mark {
    display: flex; align-items: center; gap: 10px; margin: 0 auto 44px 110px;
  }
  .back .mark-dot { width: 14px; height: 14px; background: var(--brown); }
  .back .mark-name { font-size: 16px; color: var(--brown); }
  .person {
    font-family: "Michroma", sans-serif; font-size: 19px; letter-spacing: 1px;
    text-align: right;
  }
  .degree {
    font-family: "Saira", sans-serif; font-weight: 300; font-size: 15px;
    text-align: right; margin-top: 2px;
  }
  .back .brown-field {
    flex: 1; padding: 34px 30px 0 0;
    font-family: "Saira", sans-serif; font-weight: 300; font-size: 16px;
    line-height: 1.55; text-align: right; font-style: normal;
  }
</style>
</head>
<body>
<main class="sheet">
  <section class="card front">
    <div class="brown-field">
      <span class="mark-dot"></span>
      <span class="mark-name">EQUIVITA</span>
    </div>
    <div class="white-field">
      <h1 class="brand">EQUIVITA</h1>
      <ul class="services">
        <li>Pferdezahnbehandlung</li>
        <li>Pferdefütterungsberatung</li>
        <li class="lead">Mobile Pferdewaage</li>
      </ul>
    </div>
  </section>

  <section class="card back">
    <div class="white-field">
      <div class="mark">
        <span class="mark-dot"></span>
        <span class="mark-name">EQUIVITA</span>
      </div>
      <h2 class="person">MARLENE S. VOGT</h2>
      <p class="degree">Agrarwissenschaften (Dr. sc.)</p>
    </div>
    <address class="brown-field">
      Lindenweg 14<br>
      79899 Talbach/Hochschwarzwald<br>
      0151 4829035<br>
      kontakt@pferdegebiss-praxis.com<br>
      www.equivita-praxis.de
    </address>
  </section>
</main>
</body>
</html>
```